Bref créative
Business card/letterhead/envelopes/fax cover sheet for plastic surgery practice
Morvan Plastic Surgery
Professional
Darek Olund, M.D.
unknown at this time
morvanaestheticclinic@mailbeam.example
www.darekolundmd.example
I would like name, address, phone number, fax number, and website included on front (no email address). I would also like the Continental Guild of Cosmetic Practice logo and Board Certified logo to appear on the front. The words "Plastic and Reconstructive Surgery, Hand Surgery, Cosmetic Surgery" should appear near or under my name.
The tagline "Results worth returning for" should be included (front or back). Also, an area to write in the next appointment information should be on the back.
Continental Guild of Cosmetic Practitioners Logo
logo
Board Certification logo

```html
<!DOCTYPE html>
<html lang="en">
<head>
<meta charset="utf-8">
<title>Morvan Plastic Surgery – Business Card</title>
<link rel="stylesheet" href="https://fonts.googleapis.com/css2?family=Cinzel:wght@600&family=PT+Serif:ital,wght@0,400;0,700;1,400&display=swap">
<style>
  :root {
    --page-bg: #2b2b2d;
    --navy: #1d2f8c;
    --navy-deep: #121f63;
    --blue: #2a3fb4;
    --blue-light: #4058d0;
    --white: #ffffff;
    --paper: #f4f4f6;
    --paper-shade: #dcdde2;
    --ink: #2a2f45;
    --line: rgba(255,255,255,0.75);
    --badge-gold: #e2b74a;
    --badge-green: #3aa37a;
  }
  * { box-sizing: border-box; margin: 0; padding: 0; }
  html, body { width: 1200px; height: 901px; overflow: hidden; }
  body {
    background: var(--page-bg);
    font-family: "PT Serif", Georgia, serif;
    position: relative;
  }
  .card {
    position: absolute;
    width: 640px;
    height: 366px;
    border-radius: 4px;
    overflow: hidden;
    box-shadow: 0 14px 30px rgba(0,0,0,0.45);
  }

  /* Back: appointment card */
  .card-back {
    left: 80px; top: 60px;
    background: linear-gradient(135deg, var(--blue-light) 0%, var(--navy) 45%, var(--navy-deep) 100%);
    color: var(--white);
  }
  .appointment-title {
    text-align: center;
    font-weight: 700;
    font-size: 26px;
    letter-spacing: 0.5px;
    margin-top: 34px;
  }
  .appointment-title-rule {
    width: 460px; height: 1px; background: var(--line);
    margin: 14px auto 0;
  }
  .appointment-fields { margin: 36px 0 0 48px; width: 400px; }
  .field {
    display: flex; align-items: flex-end;
    font-size: 22px; height: 58px;
  }
  .field-label { width: 80px; }
  .field-line { flex: 1; border-bottom: 1px solid var(--line); height: 1px; margin-bottom: 6px; }
  .appointment-note {
    margin: 10px 0 0 128px;
    width: 300px;
    font-size: 11px; line-height: 1.3;
    opacity: 0.85;
  }
  .accreditation-panel {
    position: absolute;
    right: 28px; bottom: 92px;
    width: 120px; height: 60px;
    background: var(--white);
    border-radius: 3px;
    display: flex; align-items: center; justify-content: space-around;
  }
  .badge-guild { width: 40px; height: 28px; background: var(--badge-gold); border-radius: 3px; }
  .badge-board { width: 34px; height: 34px; border-radius: 50%; border: 3px solid var(--badge-green); }

  /* Front: identity card */
  .card-front {
    left: 480px; top: 470px;
    background: linear-gradient(160deg, var(--white) 0%, var(--paper) 55%, var(--paper-shade) 100%);
    color: var(--ink);
  }
  .brand {
    position: absolute; top: 34px; left: 0; width: 100%;
    text-align: center;
  }
  .brand-name {
    display: inline-flex; align-items: center; gap: 12px;
    font-family: "Cinzel", "Times New Roman", serif;
    font-weight: 600; font-size: 50px; letter-spacing: 4px;
    color: var(--navy); line-height: 1;
  }
  .brand-mark { width: 14px; height: 14px; border-radius: 50%; background: var(--navy); }
  .brand-sub {
    font-family: "Cinzel", "Times New Roman", serif;
    font-weight: 600; font-size: 17px; letter-spacing: 3px;
    color: var(--navy); margin-top: 6px;
  }
  .tagline {
    font-size: 17px; color: var(--blue); margin-top: 2px; letter-spacing: 0.3px;
  }
  .name-band {
    position: absolute; top: 170px; left: 0; width: 100%; height: 54px;
    background: linear-gradient(90deg, var(--navy-deep), var(--blue) 50%, var(--navy-deep));
    color: var(--white);
    display: flex; align-items: center; padding-left: 36px;
  }
  .doctor-name { font-weight: 700; font-size: 21px; letter-spacing: 0.3px; }
  .band-divider {
    width: 2px; height: 38px; background: var(--white);
    transform: skewX(-18deg); margin: 0 14px;
  }
  .specialties { font-size: 12.5px; line-height: 1.3; }
  .contact {
    position: absolute; top: 240px; left: 0; width: 100%;
    text-align: center; font-size: 14.5px; line-height: 1.75; color: var(--ink);
  }
  .contact-label { color: var(--navy); font-weight: 700; }
</style>
</head>
<body>

<section class="card card-back" aria-label="Appointment card, back">
  <h2 class="appointment-title">Next Appointment</h2>
  <div class="appointment-title-rule"></div>
  <div class="appointment-fields">
    <div class="field"><span class="field-label">For :</span><span class="field-line"></span></div>
    <div class="field"><span class="field-label">Date :</span><span class="field-line"></span></div>
    <div class="field"><span class="field-label">Time :</span><span class="field-line"></span></div>
  </div>
  <p class="appointment-note">Please give 24 hours notice to cancel or reschedule</p>
  <div class="accreditation-panel" role="img" aria-label="Continental Guild of Cosmetic Practice badge and board certification badge">
    <span class="badge-guild"></span>
    <span class="badge-board"></span>
  </div>
</section>

<section class="card card-front" aria-label="Business card, front">
  <div class="brand">
    <div class="brand-name"><span class="brand-mark"></span>MORVAN</div>
    <div class="brand-sub">PLASTIC SURGERY</div>
    <div class="tagline">Results worth returning for</div>
  </div>
  <div class="name-band">
    <span class="doctor-name">Darek Olund, M.D.</span>
    <span class="band-divider"></span>
    <span class="specialties">Plastic &amp; Reconstructive Surgery,<br>Hand Surgery, Cosmetic Surgery</span>
  </div>
  <div class="contact">
    <div>Unit 48 Harlow Street, Elmstate, Zip 7150, Country</div>
    <div><span class="contact-label">P :</span> 555 018 3042 &nbsp;<span class="contact-label">F :</span> 555 018 6617 &nbsp;<span class="contact-label">E :</span> morvanaestheticclinic@mailbeam.example</div>
    <div><span class="contact-label">W :</span> www.darekolundmd.example</div>
  </div>
</section>

</body>
</html>
```